Website Re-design

Hi, I'm looking for help in redesigning my web site. I currently have a site www.brightmoorlamps.example where I sell lamps, and while I like some aspects of the design, you can tell that I have done the graphics myself and am not a pro at it. I'd like help in redesigning it, and am open to completely new design graphics. I have made the 3 slider images myself, and I feel they could be a bit better, but I am not sure how to do it. For example, on the homepage, the 'About Us', 'Secured Shopping', and '$10 Off' graphics don't go well with the rest of the page. I would like more cohesion in the design and more visual interest in the header, which is pretty basic right now. Also, that the bottom footer is black, I would like instead something else. I am looking for just the layout of the homepage, and possibly once that is done to work on more visual interest in some of the informational pages and product pages. I am looking for just the design in the form of a photoshop file or files that I can incorporate into my site. Thank you!
Updates

Project Deadline Extended
Reason: I just made this project payment committed, so I'd like a chance for designers who only choose payment committed projects to submit artwork. Thank you.

This project is now payment guaranteed/ committed.  Thanks.

Industry/Entity Type

Shopping

```html
<!DOCTYPE html>
<html lang="en">
<head>
<meta charset="utf-8">
<title>Brightmoor Lamps – Home</title>
<link href="https://fonts.googleapis.com/css2?family=Ubuntu:wght@300;400;500;700&display=swap" rel="stylesheet">
<style>
  :root{
    --ink:#3d3d3d;
    --muted:#6b6b6b;
    --soft:#8a8a8a;
    --teal:#1f9a9c;
    --teal-deep:#2b8f97;
    --nav:#3b3b3b;
    --nav-dark:#2c2c2c;
    --line:#d8d8d8;
    --panel:#f0f0f0;
    --white:#ffffff;
    --gold:#f3c53f;
    --gold-deep:#d9a21f;
    --banner:#6a6a6a;
  }
  *{box-sizing:border-box;margin:0;padding:0}
  html,body{width:1062px;height:1200px;overflow:hidden;background:var(--white)}
  body{font-family:"Ubuntu",sans-serif;color:var(--ink);position:relative}
  .abs{position:absolute}

  /* header */
  .site-header{position:absolute;left:0;top:0;width:1062px;height:110px;background:linear-gradient(#fff 60%,#f1f1f1)}
  .brand{position:absolute;left:90px;top:22px;display:flex;align-items:center;gap:10px}
  .brand-mark{width:48px;height:48px;border:3px solid #555;border-radius:50%}
  .brand-name{font-size:26px;font-weight:500;color:#555;line-height:26px}
  .cart-box{position:absolute;left:753px;top:19px;width:222px;height:71px;background:#eeeeee;border-radius:3px}
  .cart-label{position:absolute;left:22px;top:12px;font-size:13px;font-weight:500;color:#666}
  .cart-icon{position:absolute;left:30px;top:32px}
  .cart-divider{position:absolute;left:85px;top:8px;width:1px;height:55px;background:#d0d0d0}
  .cart-info{position:absolute;left:102px;top:9px;font-size:11.5px;line-height:20px;color:#444}
  .cart-info a{color:#8a8a8a;text-decoration:none}

  /* nav */
  .main-nav{position:absolute;left:0;top:111px;width:1062px;height:44px;background:linear-gradient(var(--nav),var(--nav-dark));border-top:1px solid #222}
  .main-nav ul{list-style:none;display:flex;position:absolute;left:87px;top:0;height:44px;align-items:center}
  .main-nav li{font-size:13.5px;font-weight:500;color:#fff;padding:0 22px;border-left:1px solid #555;line-height:24px}
  .main-nav li:first-child{border-left:none}
  .search{position:absolute;left:751px;top:7px;width:214px;height:30px;background:#fff;border-radius:2px}
  .search span{position:absolute;left:10px;top:7px;font-size:12.5px;color:#999;font-weight:300}
  .search-btn{position:absolute;right:4px;top:4px;width:22px;height:22px;background:#555;border-radius:2px}

  /* hero */
  .hero{position:absolute;left:0;top:155px;width:1062px;height:411px;overflow:hidden}
  .hero-scene{position:absolute;inset:0;background:
      radial-gradient(ellipse 380px 300px at 850px 170px,#9fe0e2 0%,rgba(159,224,226,0) 70%),
      linear-gradient(180deg,#48a9ad 0%,#5bbfc2 55%,#a9e4e6 70%,#cfd6d8 71%,#b8c1c4 100%)}
  .hero h1{position:absolute;left:109px;top:52px;font-size:29px;font-weight:700;color:#fff;letter-spacing:-.3px}
  .hero p{position:absolute;left:110px;top:96px;width:408px;font-size:13.5px;line-height:22px;color:#fff;font-weight:400}
  .hero-btn{position:absolute;top:179px;height:44px;background:#fff;border-radius:2px;font-size:20px;font-weight:300;color:#555;display:flex;align-items:center;justify-content:center}
  .callout{position:absolute;left:540px;top:163px;width:300px;height:89px;background:rgba(235,250,250,.85);clip-path:polygon(36px 0,100% 0,100% 100%,0 100%)}
  .callout .kicker{position:absolute;left:46px;top:20px;font-size:17px;color:var(--teal);font-weight:500}
  .callout .product{position:absolute;left:46px;top:47px;font-size:18px;color:#333;font-weight:400}
  .dots{position:absolute;left:493px;top:383px;display:flex;gap:8px}
  .dots i{width:12px;height:12px;border-radius:50%;background:#8c8c8c;border:1px solid #777}
  .dots i:first-child{background:#3a3a3a}

  /* products */
  .section-title{position:absolute;left:98px;top:594px;font-size:26px;font-weight:300;color:var(--teal)}
  .next-btn{position:absolute;left:941px;top:599px;width:21px;height:21px;border-radius:50%;background:#eee;border:1px solid #ddd}
  .card{position:absolute;top:645px;width:277px;height:151px;border:1px solid #ddd;background:#fff}
  .card-photo{position:absolute;left:4px;top:4px;width:118px;height:141px}
  .card-title{position:absolute;left:136px;top:18px;font-size:15px;line-height:22px;color:#666;font-weight:300}
  .card-price{position:absolute;left:136px;top:76px;font-size:14.5px;color:var(--teal)}
  .add-cart{position:absolute;left:136px;top:112px;font-size:15px;color:#222;display:flex;align-items:center;gap:9px}

  /* newsletter */
  .newsletter{position:absolute;left:97px;top:825px;width:868px;height:68px;background:linear-gradient(#777,#5f5f5f);border-radius:2px}
  .seal{position:absolute;left:96px;top:821px;width:76px;height:76px;border-radius:50%;background:radial-gradient(circle,var(--gold) 55%,var(--gold-deep) 100%);border:2px dotted #e3ae2a;text-align:center;color:#b34a12;font-weight:700}
  .seal b{display:block;margin-top:17px;font-size:19px;line-height:20px}
  .seal span{font-size:12px}
  .nl-head{position:absolute;left:190px;top:832px;color:#fff;font-weight:500}
  .nl-head strong{display:block;font-size:21px;font-weight:500;line-height:26px}
  .nl-head em{display:block;font-style:normal;font-size:16.5px;line-height:22px}
  .nl-input{position:absolute;left:502px;top:840px;width:227px;height:32px;background:#fff;border:1px solid #ccc;font-size:12.5px;color:#888;padding:7px 10px;font-weight:300}
  .nl-btn{position:absolute;left:733px;top:840px;width:87px;height:32px;background:linear-gradient(#fbd35a,#e9b22c);border-radius:2px;color:#3a3a3a;font-size:13.5px;font-weight:500;display:flex;align-items:center;justify-content:center}
  .nl-note{position:absolute;left:844px;top:840px;width:115px;font-size:11.5px;line-height:17px;color:#eee;font-weight:300}

  /* footer links */
  .rule{position:absolute;left:89px;top:926px;width:885px;height:1px;background:var(--line)}
  .col{position:absolute;top:952px}
  .col h3{font-size:14px;font-weight:400;color:#333;margin-bottom:7px}
  .col ul{list-style:none}
  .col li{font-size:12px;line-height:22px;color:#777;font-weight:300;padding-left:10px;position:relative}
  .col li::before{content:"";position:absolute;left:0;top:10px;width:3px;height:3px;background:#aaa;border-radius:50%}
  .ssl{position:absolute;left:857px;top:1035px;width:117px;height:38px;border:1px solid #bbb;background:#fafafa}
  .ssl::before{content:"";position:absolute;left:0;top:0;width:17px;height:100%;background:#555}
  .ssl::after{content:"";position:absolute;left:24px;top:7px;width:22px;height:22px;border-radius:50%;background:#e8c24a}
  .pay{position:absolute;top:1090px;width:24px;height:16px;border:1px solid #ccc;border-radius:2px}

  /* bottom */
  .bottom-bar{position:absolute;left:0;top:1136px;width:1062px;height:64px;background:var(--panel);border-top:1px solid #ddd}
  .copyright{position:absolute;left:96px;top:23px;font-size:12px;color:#333;font-weight:300}
  .social{position:absolute;top:20px;width:21px;height:21px;border-radius:3px}
</style>
</head>
<body>

<header class="site-header">
  <div class="brand">
    <div class="brand-mark"></div>
    <div class="brand-name">brightmoor<br>lamps</div>
  </div>
  <div class="cart-box">
    <div class="cart-label">My Cart</div>
    <svg class="cart-icon" width="34" height="30" viewBox="0 0 34 30"><path d="M1 3h6l4 16h16l3-11H9" fill="none" stroke="#555" stroke-width="2.4"/><circle cx="13" cy="25" r="2.6" fill="#555"/><circle cx="25" cy="25" r="2.6" fill="#555"/></svg>
    <div class="cart-divider"></div>
    <div class="cart-info">(0) items in your cart<br>Total - $ 00.00<br><a>My Account</a> &nbsp;|&nbsp; <a>My List</a></div>
  </div>
</header>

<nav class="main-nav">
  <ul>
    <li>HOME</li><li>ABOUT US</li><li>PRODUCTS</li><li>CONTACT US</li><li>REGISTER</li><li>SIGN IN</li>
  </ul>
  <div class="search"><span>Search products...</span>
    <div class="search-btn"><svg width="22" height="22" viewBox="0 0 22 22"><circle cx="10" cy="10" r="4.5" fill="none" stroke="#fff" stroke-width="2"/><path d="M13.3 13.3l4 4" stroke="#fff" stroke-width="2.2"/></svg></div>
  </div>
</nav>

<section class="hero">
  <div class="hero-scene" role="img" aria-label="Photo of a turquoise glass table lamp with a white shade standing on a whitewashed wooden floor against a teal wall"></div>
  <h1>WELCOME TO BRIGHTMOOR LAMPS</h1>
  <p>Brightmoor Lamps was born out of an enthusiasm for creating visually enticing forms combined with a strong sense of the way that lighting sets the mood and frames a space.</p>
  <div class="hero-btn" style="left:111px;width:126px">READ MORE</div>
  <div class="hero-btn" style="left:247px;width:174px">SHOP ALL LAMPS</div>
  <div class="callout">
    <div class="kicker">LIGHT UP THE ROOM</div>
    <div class="product">“The Lagoon” Medium Table Lamp</div>
  </div>
  <div class="dots"><i></i><i></i><i></i><i></i></div>
</section>

<h2 class="section-title">OUR PRODUCTS</h2>
<div class="next-btn"><svg width="19" height="19" viewBox="0 0 19 19"><path d="M8 6l3.5 3.5L8 13" fill="none" stroke="#777" stroke-width="1.4"/></svg></div>

<article class="card" style="left:97px">
  <div class="card-photo" role="img" aria-label="Product photo of a purple cut-glass table lamp with white shade" style="background:linear-gradient(#eee,#d9d3de 60%,#cfc3d5)"></div>
  <div class="card-title">Violet Facet<br>Table Lamp</div>
  <div class="card-price">$219.00</div>
  <div class="add-cart"><svg width="24" height="20" viewBox="0 0 24 20"><path d="M0 2h4l3 11h13l2-8H6" fill="#222" stroke="#222" stroke-width="1.5"/><circle cx="9" cy="17" r="2" fill="#222"/><circle cx="18" cy="17" r="2" fill="#222"/></svg>ADD TO CART</div>
</article>
<article class="card" style="left:392px">
  <div class="card-photo" role="img" aria-label="Product photo of a turquoise and green glass table lamp with white shade" style="background:linear-gradient(#eee,#d5e8e4 60%,#c2e0d4)"></div>
  <div class="card-title">Violet Facet<br>Table Lamp</div>
  <div class="card-price">$219.00</div>
  <div class="add-cart"><svg width="24" height="20" viewBox="0 0 24 20"><path d="M0 2h4l3 11h13l2-8H6" fill="#222" stroke="#222" stroke-width="1.5"/><circle cx="9" cy="17" r="2" fill="#222"/><circle cx="18" cy="17" r="2" fill="#222"/></svg>ADD TO CART</div>
</article>
<article class="card" style="left:688px">
  <div class="card-photo" role="img" aria-label="Product photo of a clear glass bulbous lamp with a gold shade" style="background:linear-gradient(#eee,#e2d8c8 60%,#d8ccb8)"></div>
  <div class="card-title">Violet Facet<br>Table Lamp</div>
  <div class="card-price">$219.00</div>
  <div class="add-cart"><svg width="24" height="20" viewBox="0 0 24 20"><path d="M0 2h4l3 11h13l2-8H6" fill="#222" stroke="#222" stroke-width="1.5"/><circle cx="9" cy="17" r="2" fill="#222"/><circle cx="18" cy="17" r="2" fill="#222"/></svg>ADD TO CART</div>
</article>

<section class="newsletter"></section>
<div class="seal"><b>10%</b><span>OFFER</span></div>
<div class="nl-head"><strong>$10 off any purchase</strong><em>when you sign up for our newsletter.</em></div>
<div class="nl-input">Enter your E-mail ID</div>
<div class="nl-btn">SUBSCRIBE</div>
<div class="nl-note">Coupon code will be sent to your inbox.</div>

<div class="rule"></div>
<div class="col" style="left:95px"><h3>Help + Info</h3><ul><li>Contact Us</li><li>Shipping Info</li><li>Returns</li><li>To The Trade</li><li>Privacy Policy</li><li>Terms of Use</li></ul></div>
<div class="col" style="left:224px"><h3>My Account</h3><ul><li>Sign in</li><li>Order Status</li><li>Order History</li><li>View Cart</li><li>Checkout</li></ul></div>
<div class="col" style="left:364px"><h3>About</h3><ul><li>Who we are</li><li>Testimonials</li></ul></div>
<div class="col" style="left:494px"><h3>Contact</h3><ul><li>Contact us</li><li>info@brightmoorlamps.example</li></ul></div>
<div class="col" style="left:670px"><h3>Secure Shopping</h3><ul><li>We Value Your Privacy</li><li>Secure Shopping</li><li>About Cookies</li><li>Personal Information Collected</li><li>Our Email List</li><li>Protecting Children</li></ul></div>
<div class="col" style="left:857px;top:981px"><ul><li>Links To Other Sites</li><li>Policy Changes</li></ul></div>
<div class="ssl"></div>
<div class="pay" style="left:857px;background:#dfe6f1"></div>
<div class="pay" style="left:888px;background:#d9dde8"></div>
<div class="pay" style="left:919px;background:#ececec"></div>
<div class="pay" style="left:950px;background:#cfd6ea"></div>

<footer class="bottom-bar">
  <div class="copyright">Copyright &nbsp;© 2013 &nbsp;Brightmoor Lamps. &nbsp; All rights reserved.</div>
  <div class="social" style="left:922px;background:#3b5a98"></div>
  <div class="social" style="left:950px;background:#3fb3e6"></div>
</footer>

</body>
</html>
```